Meridale Hair Studio Needs a new appointment business card

We need a new appointment card for our hair salon.

I Dont want bright out there colours.
I would like it to be neat, clean, easy to read. White, Black, with a hint of colour if needed.

We need
-Logo
-Phone number 47260385
-Mobile Number: 0417360528
Address: Shop 3/217 Tarrow Street, Kelby Court, Mackay 4740

BACK SIDE OF CARD
- Appointment Time & Date (White background so we are able to write on it)
(If you are unable to make your appointment please contact us ASAP 47260385)

I also would like the chatterly and Snapfold logo(Find us on Chatterly)(find us on Snapfold)

Target Market(s)

appointment card simple to read. all information for their next appoint For all our clients male and female

Industry/Entity Type

Hairdresser

Contact Information for Business Card

-Logo
-Phone number 47260385

BACK SIDE OF CARD

Font styles to use
Serif
Sans Serif
Script

Requirements
Must have
• White Back ground on backside with appointment deatils so we are able to write information (like appointment time and date)
Nice to have
• Find us on Chatterly
and
snapfold - meridale_hairstudio
Should not have
• BRIGHT COLOURS

```html
<!DOCTYPE html>
<html lang="en">
<head>
<meta charset="utf-8">
<title>Meridale Hair Studio – Appointment Card (Back)</title>
<link rel="stylesheet" href="https://fonts.googleapis.com/css2?family=Nunito+Sans:ital,wght@0,400;0,700;0,800;1,400;1,800&display=swap">
<style>
  :root {
    --page-bg: #ffffff;
    --card-bg: #f4f4f4;
    --ink: #111111;
    --ink-soft: #2a2a2a;
    --write-area: #f4f4f4;
  }
  * { margin: 0; padding: 0; box-sizing: border-box; }
  html, body {
    width: 1200px;
    height: 686px;
    overflow: hidden;
    background: var(--page-bg);
  }
  body {
    position: relative;
    font-family: "Nunito Sans", Arial, sans-serif;
    color: var(--ink);
  }
  .card-back {
    position: absolute;
    left: 42px;
    top: 42px;
    width: 1116px;
    height: 600px;
    background: var(--card-bg);
  }
  .appointment-table {
    position: absolute;
    left: 101px;
    top: 190px;
    width: 912px;
    height: 81px;
    display: flex;
    border: 3px solid var(--ink);
    background: var(--write-area);
  }
  .appointment-field {
    flex: 1;
    padding: 6px 0 0 14px;
    font-weight: 700;
    font-size: 23px;
  }
  .appointment-field + .appointment-field {
    border-left: 3px solid var(--ink);
  }
  .cancellation-note {
    position: absolute;
    left: 0;
    top: 300px;
    width: 100%;
    text-align: center;
    font-style: italic;
    font-size: 18px;
    letter-spacing: 0.06em;
    color: var(--ink-soft);
  }
  .cancellation-note strong {
    font-style: normal;
    font-weight: 800;
    color: var(--ink);
  }
  .social-footer {
    position: absolute;
    right: 38px;
    top: 546px;
    display: flex;
    align-items: center;
    gap: 14px;
    font-size: 17px;
  }
  .social-intro {
    font-weight: 400;
    margin-right: 6px;
  }
  .social-network {
    display: flex;
    align-items: center;
    gap: 6px;
    font-weight: 700;
  }
  .social-network svg { display: block; }
  .social-handle {
    margin-left: 8px;
    font-weight: 800;
    font-style: italic;
    font-size: 18px;
  }
</style>
</head>
<body>
  <main class="card-back">
    <section class="appointment-table">
      <div class="appointment-field">Date</div>
      <div class="appointment-field">Time</div>
    </section>

    <p class="cancellation-note">(If you are unable to make your appointment please contact us <strong>ASAP 47260385</strong>)</p>

    <footer class="social-footer">
      <span class="social-intro">Find us on</span>
      <span class="social-network">
        <svg width="14" height="14" viewBox="0 0 14 14" aria-hidden="true"><circle cx="7" cy="7" r="7" fill="var(--ink)"/></svg>
        Chatterly
      </span>
      <span class="social-network">
        <svg width="14" height="14" viewBox="0 0 14 14" aria-hidden="true"><circle cx="7" cy="7" r="7" fill="var(--ink)"/></svg>
        Snapfold
      </span>
      <span class="social-handle">meridale_hairstudio</span>
    </footer>
  </main>
</body>
</html>
```